We Need a Letterhead + Fax Cover Sheet for Heron Staffing

LETTERHEAD:
- Simple letterhead. Please provide an editable .doc file apart from usual Source Files. Logo Files attached for your use.
- Please place our logo on the upper right corner of the page. You may add some sort of graphic, or light colored background (depends on what looks good).
- Footer should include:
Heron Staffing, LLC
412 Kestrel Ave. Suite 118
Port Alden, GA 31522

FAX COVER SHEET:
- Have the logo placed here, should be large, maybe an eight of the page.
- Put:
From:
To:
Phone Number:
Fax Number:

*Still needs some details, will update you because working on the website, etc.

Heron Coastal Workforce Services

```html
<!DOCTYPE html>
<html lang="en">
<head>
<meta charset="utf-8">
<title>Heron Staffing – Letterhead and Fax Cover Sheet</title>
<link href="https://fonts.googleapis.com/css2?family=Open+Sans:wght@300;400;600;700&family=Cormorant+Garamond:ital,wght@1,600&family=Tinos&display=swap" rel="stylesheet">
<style>
  :root {
    --bg-top: #ffffff;
    --bg-bottom: #c4c4c4;
    --paper: #ffffff;
    --ink: #333333;
    --ink-soft: #444444;
    --brand-blue: #0a72b0;
    --brand-green: #7aa23a;
    --rule-blue: #b9dcef;
    --faint-mark: #eef1e4;
  }
  * { margin: 0; padding: 0; box-sizing: border-box; }
  html, body { width: 1200px; height: 1200px; overflow: hidden; }
  body {
    position: relative;
    background: linear-gradient(to bottom, var(--bg-top) 0%, #eeeeee 35%, var(--bg-bottom) 100%);
    font-family: "Open Sans", sans-serif;
    color: var(--ink);
  }
  .board-label {
    position: absolute;
    font-weight: 400;
    font-size: 28px;
    letter-spacing: 0.5px;
    color: #222;
    text-align: center;
    width: 544px;
    line-height: 1;
  }
  .board-label--letterhead { left: 50px; top: 192px; }
  .board-label--fax { left: 616px; top: 188px; }

  .sheet {
    position: absolute;
    background: var(--paper);
    box-shadow: 3px 4px 8px rgba(0,0,0,0.35);
    overflow: hidden;
  }
  .sheet--letterhead { left: 46px; top: 249px; width: 544px; height: 761px; }
  .sheet--fax { left: 611px; top: 249px; width: 546px; height: 764px; }

  .brand-mark {
    position: absolute;
    top: 24px;
    right: 24px;
    width: 98px;
    text-align: center;
  }
  .brand-mark__dot {
    width: 26px; height: 26px;
    border-radius: 50%;
    background: var(--brand-blue);
    margin: 0 auto 6px;
  }
  .brand-mark__name {
    font-weight: 700;
    font-size: 12px;
    line-height: 1.2;
    text-transform: uppercase;
    color: var(--brand-blue);
  }

  .faint-emblem {
    position: absolute;
    right: 24px;
    bottom: 24px;
    width: 186px;
    height: 190px;
  }

  .footer-band {
    position: absolute;
    left: 0; right: 0; bottom: 0;
    height: 25px;
    background: var(--brand-blue);
  }
  .footer-contact {
    position: absolute;
    left: 34px;
    bottom: 37px;
  }
  .footer-contact__company {
    font-family: "Cormorant Garamond", serif;
    font-style: italic;
    font-weight: 600;
    font-size: 17px;
    letter-spacing: 0.6px;
    color: var(--brand-green);
    margin-bottom: 4px;
  }
  .footer-contact__address {
    font-family: "Tinos", serif;
    font-size: 13px;
    color: var(--ink-soft);
  }

  .fax-title {
    position: absolute;
    left: 41px;
    top: 80px;
    font-weight: 600;
    font-size: 26px;
    line-height: 1;
    letter-spacing: 3.4px;
    color: var(--ink);
  }
  .fax-title-rule {
    position: absolute;
    left: 37px;
    top: 121px;
    width: 295px;
    height: 1px;
    background: var(--rule-blue);
  }
  .fax-fields {
    position: absolute;
    left: 37px;
    top: 173px;
    width: 467px;
    list-style: none;
  }
  .fax-field {
    position: absolute;
    left: 0;
    width: 100%;
    display: flex;
    align-items: baseline;
    font-size: 13px;
    color: var(--ink);
    letter-spacing: 0.3px;
  }
  .fax-field::after {
    content: "";
    flex: 1;
    margin-left: 5px;
    border-bottom: 2px dotted #666;
    transform: translateY(-2px);
  }
</style>
</head>
<body>
  <h2 class="board-label board-label--letterhead">LETTERHEAD</h2>
  <h2 class="board-label board-label--fax">FAX COVER SHEET</h2>

  <section class="sheet sheet--letterhead" aria-label="Letterhead">
    <div class="brand-mark">
      <div class="brand-mark__dot"></div>
      <div class="brand-mark__name">Heron Coastal Workforce Services</div>
    </div>
    <svg class="faint-emblem" viewBox="0 0 186 190" role="img" aria-label="Faint brand emblem decoration">
      <circle cx="93" cy="95" r="90" fill="var(--faint-mark)"/>
    </svg>
    <div class="footer-contact">
      <p class="footer-contact__company">Heron Staffing, LLC</p>
      <p class="footer-contact__address">412 Kestrel Ave. Suite 118Port Alden, GA 31522</p>
    </div>
    <div class="footer-band"></div>
  </section>

  <section class="sheet sheet--fax" aria-label="Fax cover sheet">
    <div class="brand-mark">
      <div class="brand-mark__dot"></div>
      <div class="brand-mark__name">Heron Coastal Workforce Services</div>
    </div>
    <h1 class="fax-title">FAX COVER SHEET</h1>
    <div class="fax-title-rule"></div>
    <ul class="fax-fields">
      <li class="fax-field" style="top:0;">To</li>
      <li class="fax-field" style="top:36px;">From</li>
      <li class="fax-field" style="top:72px;">Re</li>
      <li class="fax-field" style="top:125px;">Fax Number</li>
      <li class="fax-field" style="top:170px;">Phone Number</li>
      <li class="fax-field" style="top:211px;">Pages</li>
      <li class="fax-field" style="top:255px;">Date</li>
    </ul>
    <svg class="faint-emblem" viewBox="0 0 186 190" role="img" aria-label="Faint brand emblem decoration">
      <circle cx="93" cy="95" r="90" fill="var(--faint-mark)"/>
    </svg>
    <div class="footer-contact">
      <p class="footer-contact__company">Heron Staffing, LLC</p>
      <p class="footer-contact__address">412 Kestrel Ave. Suite 118Port Alden, GA 31522</p>
    </div>
    <div class="footer-band"></div>
  </section>
</body>
</html>
```